Vertriebsweg.de

The nordische-policenmarkt.de (npm) is an internet portal for the incurance industry in Germany: www.nordische-policenmarkt.de.

We are now planning to start a new brand Vertriebswege.de, which will be integral part of npm, but will have own logo, navigation etc. The main topic of Vertriebswege.de will be the new digital way of communication between insurance companies and insurance brokers (selling companies' products).

The main content of Vertriebswege.de will consist of articles / blog entries and at this moment we would like to concentrate on that part of our new brand.

At the top of the page we will always have a cover story, which will be the latest published article.

Under the cover story the user will find other articles. The articles should have variable widths (1/3, 2/3, 3/3). We will also need some additional elements like newsletter subscription, articles with most clicks etc.

Please use as reference this page:
https://www.kalmer.example/

We really like how it is designed.

Here you will find the current state of our project:

https://relaunch.nordische-policenmarkt.de/vertriebswege

We will also need a logo for Vertriebswege.de, which should include the subtitle: Immer unabhängig, niemals neutral AND powerd by nordische-policenmarkt.de
Updates

Due to the problems with the "Pool" functionality at SketchHarbor we will need more time to verify your projects in our teem - but we are on it.

```html
<!DOCTYPE html>
<html lang="de">
<head>
<meta charset="utf-8">
<title>Vertriebswege – Artikel</title>
<link href="https://fonts.googleapis.com/css2?family=Poppins:wght@400;500;600;700&display=swap" rel="stylesheet">
<style>
:root{--red:#e3231b;--ink:#111;--text:#333;--muted:#8a8a8a;--line:#cfcfcf;--footer:#000;}
*{box-sizing:border-box;margin:0;padding:0}
html,body{width:1200px;height:2694px;overflow:hidden;background:#fff;font-family:'Poppins',sans-serif;color:var(--text)}
.page{position:relative;width:1200px;height:2694px}
.abs{position:absolute}
.topbar{left:660px;top:0;width:540px;height:40px;background:var(--red);clip-path:polygon(18px 0,100% 0,100% 100%,0 100%);display:flex;align-items:center;padding-left:40px;gap:0;color:#fff;font-size:14px;font-weight:600}
.topbar span{padding:0 28px;border-right:1px solid rgba(255,255,255,.7);line-height:16px;display:flex;align-items:center;gap:7px}
.topbar span:last-child{border:0}
.logo{display:flex;align-items:center;gap:6px;color:var(--red);font-weight:700;font-size:29px;letter-spacing:.5px}
.logo i{display:block;width:24px;height:24px;background:var(--red);border-radius:5px}
.nav{left:516px;top:66px;display:flex;gap:32px;font-size:16px;font-weight:500;color:#222;letter-spacing:.2px}
.search{left:1059px;top:56px;width:42px;height:42px;border-radius:50%;background:#555}
.photo{left:79px;top:189px;width:386px;height:438px;background:linear-gradient(135deg,#b9b4ae,#6d6660 55%,#2b2a2c)}
.badge{left:486px;top:189px;background:var(--red);color:#fff;font-size:12px;font-weight:600;padding:6px 14px;border-radius:3px}
.date{left:486px;top:228px;font-size:15px;color:#333;display:flex;gap:6px;align-items:center}
.headline{left:486px;top:266px;width:620px;font-size:22px;font-weight:500;line-height:34px;color:var(--ink)}
.lead{left:486px;top:341px;width:620px;font-size:16px;font-weight:500;line-height:30px;color:#222}
.col{left:486px;top:451px;width:620px;font-size:16px;line-height:30.3px}
.body p{font-size:16px;line-height:30.3px;margin-bottom:15px}
.body{left:79px;top:656px;width:1025px}
.cm-title{left:0;width:1200px;top:1390px;text-align:center;font-size:29px;font-weight:600;color:var(--ink)}
.field{border:2px solid #cfcfcf;border-radius:3px;font-size:16px;color:#333;padding:0 16px;display:flex;align-items:center}
.consent{left:234px;top:1868px;display:flex;gap:10px;align-items:center;font-size:15px}
.consent i{width:17px;height:17px;border:1px solid #aaa;display:block}
.btn{background:var(--red);color:#fff;font-weight:600;font-size:14px;letter-spacing:.5px;display:flex;align-items:center;justify-content:center;border-radius:3px}
.note{left:234px;top:2062px;width:740px;font-size:13.5px;line-height:27.5px;color:#222}
.footer{left:0;top:2292px;width:1200px;height:402px;background:var(--footer)}
.nl{left:186px;top:2246px;width:829px;height:142px;background:var(--red)}
.nl small{position:absolute;left:29px;top:54px;color:#fff;font-size:15px;font-weight:600;letter-spacing:1px}
.nl b{position:absolute;left:29px;top:70px;color:#fff;font-size:28px;font-weight:600}
.nl .sep{position:absolute;left:246px;top:40px;width:1px;height:64px;background:rgba(255,255,255,.6)}
.fh{color:#fff;font-size:22px;font-weight:600}
.flinks{display:grid;grid-template-columns:120px 120px;row-gap:16px;font-size:15px;color:#bbb}
.flinks span::before{content:"› ";color:var(--red);font-weight:700}
.social div{display:flex;align-items:center;gap:16px;color:#bbb;font-size:15px;margin-bottom:15px}
.social i{display:block;width:42px;height:42px;border-radius:50%;background:var(--red)}
.vline{width:1px;background:#333;top:2445px;height:192px}
</style>
</head>
<body>
<div class="page">
  <div class="abs topbar"><span>▤ MEDIA DATA</span><span>➤ NEWSLETTER</span><span>● LOGIN</span></div>
  <div class="abs logo" style="left:80px;top:40px"><i></i>VERTRIEBSWEGE</div>
  <nav class="abs nav"><span>PROCESS MESSAGES</span><span>MVP SYSTEMS</span><span>EVENTS</span><span>STUDIES</span></nav>
  <div class="abs search"><svg width="42" height="42" viewBox="0 0 42 42"><circle cx="20" cy="20" r="7" fill="none" stroke="#fff" stroke-width="2"/><line x1="25" y1="25" x2="29" y2="29" stroke="#fff" stroke-width="2"/></svg></div>

  <div class="abs photo" role="img" aria-label="Portrait eines Geschäftsmanns im Anzug mit Laptop"></div>
  <div class="abs badge">CATEGORIES</div>
  <div class="abs date"><svg width="13" height="13" viewBox="0 0 13 13"><rect x="1" y="2" width="11" height="10" fill="#333"/><rect x="2" y="5" width="9" height="6" fill="#fff"/></svg>27 May 2021</div>
  <h1 class="abs headline">Lorem ipsum dolor sit amet, consectetur adipisicing elit, sed do eiusmod tempor incididunt ut labore et.</h1>
  <p class="abs lead">Lorem ipsum dolor sit amet consectetur adipisicing elit sed do eiusmod tempor incididunt ut labore et dolore magna aliqua. Ut enim ad minim veniam, quis nostrud exercitation ullamco laboris nisi ut aliquip.</p>
  <p class="abs col">Duis aute irure dolor in reprehenderit in voluptate velit esse cillum dolore eu fugiat nulla pariatur. Excepteur sint occaecat cupidatat non proident, sunt in culpa qui officia deserunt mollit anim id est laborum. Sed ut perspiciatis sew unde omnis iste natus error sit voluptatem accusantium doloremque conco laudantium, totam rem aperiam, eaque ipsa quae ab illo inventore veritatis et quasi architecto beatae vitae dicta sunt explicabo.</p>

  <div class="abs body">
    <p>&nbsp;Nemo enim ipsam voluptatem quia voluptas sit aspernatur aut odit aut fugit, sed quia consequuntur magni dolores eos qui ratione voluptatem sequi nesciunt. Neque porro quisquam est, qui dolorem ipsum quia dolor sit amet, consectetur, adipisci velit, sed quia non numquam eius modi tempora incidunt ut labore et dolore magnam aliquam quaerat voluptatem.</p>
    <p>Cillum dolore eu fugiat nulla pariatur. Excepteur sint occaecat cupidatat non proident, sunt in culpa qui officia deserunt mollit anim id est laborum. Sed ut perspiciatis unde omnis iste natus error sit voluptatem accusantium doloremque laudantium, totam rem aperiam, eaque ipsa quae ab illo inventore veritatis et quasi architecto beatae vitae dicta sunt explicabo. Nemo enim ipsam voluptatem quia voluptas sit aspernatur aut odit aut fugit, sed quia consequuntur magni dolores eos qui ratione voluptatem sequi nesciunt. Neque porro quisquam est, qui dolorem ipsum quia dolor sit amet, consectetur, adipisci velit, sed quia non numquam eius modi tempora incidunt ut labore et dolore magnam aliquam quaerat voluptatem.</p>
    <p>Inventore veritatis et quasi architecto beatae vitae dicta sunt explicabo. Nemo enim ipsam voluptatem quia voluptas sit aspernatur aut odit aut fugit, sed quia consequuntur magni dolores eos qui ratione voluptatem sequi nesciunt. Neque porro quisquam est, qui dolorem ipsum quia dolor sit amet, consectetur, adipisci velit, sed quia non numquam eius modi tempora incidunt ut labore et dolore magnam aliquam quaerat voluptatem. Lorem ipsum dolor sit amet, consectetur adipisicing elit, sed do eiusmod tempor incididunt ut labore et dolore magna aliqua. Ut enim ad minim veniam, quis nostrud exercitation ullamco laboris nisi ut aliquip ex ea commodo consequat. Duis aute irure dolor in reprehenderit in voluptate velit esse cillum dolore eu fugiat nulla pariatur. Excepteur sint occaecat cupidatat non proident, sunt in culpa qui officia deserunt mollit anim id est laborum. Sed ut perspiciatis unde omnis iste natus error sit voluptatem accusantium doloremque laudantium, totam rem aperiam, eaque ipsa quae ab illo inventore veritatis et quasi architecto beatae vitae dicta sunt explicabo. Nemo enim ipsam voluptatem quia voluptas sit aspernatur aut odit aut fugit, sed quia consequuntur magni dolores eos qui ratione voluptatem sequi nesciunt. Neque porro quisquam est, qui dolorem ipsum quia dolor sit amet, consectetur, adipisci velit, sed quia non numquam eius modi tempora incidunt ut labore et dolore magnam aliquam quaerat voluptatem.</p>
  </div>

  <h2 class="abs cm-title">Write a Comment</h2>
  <div class="abs field" style="left:234px;top:1478px;width:359px;height:48px">First Name*</div>
  <div class="abs field" style="left:607px;top:1478px;width:359px;height:48px">Last Name*</div>
  <div class="abs field" style="left:234px;top:1543px;width:732px;height:48px">Email Address*</div>
  <div class="abs field" style="left:234px;top:1608px;width:732px;height:246px;align-items:flex-start;padding-top:14px">Comment on the article*</div>
  <div class="abs consent"><i></i>I consent to the publication of my comment. *</div>
  <div class="abs" style="left:233px;top:1931px;font-size:15.5px">Please enter the following character string</div>
  <svg class="abs" style="left:580px;top:1918px" width="90" height="50" viewBox="0 0 90 50"><line x1="2" y1="22" x2="88" y2="36" stroke="#222" stroke-width="1"/><text x="26" y="34" font-family="Poppins,sans-serif" font-size="24" font-style="italic" fill="#222" transform="rotate(-6 45 25)">c5v9</text></svg>
  <div class="abs btn" style="left:713px;top:1919px;width:253px;height:48px">PUBLISH THE COMMENT</div>
  <div class="abs field" style="left:234px;top:1977px;width:203px;height:50px"></div>
  <p class="abs note">Lorem ipsum dolor sit amet, consectetur adipisicing elit, sed do eiusmod tempor incididunt ut labore et dolore magna aliqua. Ut enim ad minim veniam, quis nostrud exercitation ullamco laboris nisi ut aliquip commodos consequat. Duis aute irure dolor in reprehenderit in voluptate velit esse cillum dolore eu fugiat nulla.</p>
  <p class="abs" style="left:234px;top:2156px;font-size:14px;font-weight:500;color:#222">Text fields marked with * must be filled out.</p>

  <div class="abs footer"></div>
  <div class="abs nl">
    <small>Newsletter</small><b>Subscribe Us</b><span class="sep"></span>
    <div class="abs" style="left:284px;top:48px;width:314px;height:47px;background:#fff;border-radius:3px;font-size:15.5px;color:#333;padding:14px 18px">Email Address</div>
    <div class="abs btn" style="left:611px;top:48px;width:188px;height:47px;background:#000;font-size:15px;font-weight:700">SUBSCRIBE ➤</div>
  </div>

  <div class="abs logo" style="left:80px;top:2438px"><i></i>VERTRIEBSWEGE</div>
  <p class="abs" style="left:79px;top:2478px;width:380px;font-size:15.5px;line-height:30.5px;color:#9a9a9a">Lorem ipsum dolor sit amet consecteturptat adipisicing elit sed do eiusmod tempor incidi ut labore et dolore magna aliqua ut enim</p>
  <p class="abs" style="left:79px;top:2614px;font-size:14.5px;color:#bbb">© Copyright 2022 Vertriebswege</p>
  <div class="abs vline" style="left:510px"></div>
  <div class="abs vline" style="left:839px"></div>
  <div class="abs fh" style="left:576px;top:2437px">Quick Links</div>
  <div class="abs flinks" style="left:576px;top:2478px"><span>Conditions</span><span>Sitemap</span><span>Privacy</span><span>Team</span><span>Help</span><span>Media</span><span>Imprint</span><span>Data</span></div>
  <div class="abs fh" style="left:905px;top:2437px">Stay With Us</div>
  <div class="abs social" style="left:906px;top:2484px"><div><i></i>Kreisnetz</div><div><i></i>Kurzpost</div><div><i></i>Bildstrom</div></div>
</div>
</body>
</html>
```